Helicopter Tour Brochure Design (8.5 x 11" Bi-Fold Brochure)

Flyer Design for Helicopter Sightseeing Tours. Should be very inviting and touristy. Read "must have" section for more information.

Target Market(s)

Tourists visiting Florida

Industry/Entity Type

Aviation

Colors
3176b5
0456a4
85acd3
757575
9d9d9d
1b1b1b

Requirements
Must have
• Must include the Tour photos and "Route map", so customers know where the tours travels along. It must be inviting.
• Also, design must be for a 8.5 x 11" bi-fold brochure/flyer and include a brief description about our company:
• " Corvane Aviation offers unparalleled sightseeing opportunities with a commitment to safety & customer service. The view during our sightseeing tours will provide for your comfort & more beauty than you ever imagined. And like many of our customers, you’ll want to tell your friends all about it! Corvane Aviation’s experienced pilots will provide a comfortable flight leaving you with a smile on your face. Departure location will be the Pellmont Airport, unless otherwise requested with our office. "
• You can find the tour description online at www.corvanefly.com/tours, which should be included as well.
• Must be in PDF Format.
• 8.5 x 11" Bi-Fold Brochure
• ATTACHED ARE THE DETAILED FORMAT INFORMATION.

```html
<!DOCTYPE html>
<html lang="en">
<head>
<meta charset="utf-8">
<title>Sightseeing Tours – Brochure Inside Spread</title>
<link href="https://fonts.googleapis.com/css2?family=Montserrat:wght@300;400;600;800;900&family=Oswald:wght@500&display=swap" rel="stylesheet">
<style>
  :root{
    --stage:#5b93b0;
    --brand-blue:#0456a4;
    --mid-blue:#3176b5;
    --soft-blue:#85acd3;
    --page-light:#d6e8f6;
    --page-mid:#b3d2ec;
    --ink:#1b1b1b;
    --grey:#757575;
    --white:#ffffff;
  }
  *{box-sizing:border-box;margin:0;padding:0}
  html,body{width:1200px;height:1000px;overflow:hidden}
  body{background:var(--stage);font-family:"Montserrat",sans-serif;position:relative}

  .spread{position:absolute;left:50px;top:144px;width:1100px;height:712px;overflow:hidden;
    background:linear-gradient(180deg,var(--page-light) 0%,var(--page-mid) 100%);
    box-shadow:0 14px 30px rgba(0,0,0,.25)}
  .fold{position:absolute;left:549px;top:0;width:2px;height:100%;background:rgba(4,86,164,.12)}
  .backdrop-photo{position:absolute;left:120px;top:150px;width:860px;height:500px;
    background:radial-gradient(ellipse at center,rgba(90,120,150,.28),rgba(90,120,150,0) 70%)}

  .photo{position:absolute}
  .photo-crew{left:0;top:0;width:550px;height:150px;
    background:linear-gradient(180deg,#7fb0de 0%,#cfe0ea 45%,#5e9a4a 75%,#3f7a34 100%)}
  .photo-skyline{left:550px;top:0;width:550px;height:190px;
    background:linear-gradient(180deg,#4a92d6 0%,#8ec3ea 40%,#1f5f8e 70%,#2a6f96 100%)}
  .wave{position:absolute;left:0;width:100%}
  .wave-top-left{top:112px;height:60px;width:550px}
  .wave-top-right{left:550px;width:550px;top:150px;height:50px}
  .wave-bottom{bottom:0;height:40px}

  .section-title{position:absolute;left:0;width:1100px;top:112px;text-align:center;
    font-family:"Oswald",sans-serif;font-weight:500;font-size:52px;line-height:1.1;letter-spacing:1px;color:var(--white);
    text-shadow:0 2px 6px rgba(0,0,0,.35)}

  .map-card{position:absolute;background:var(--white);border-radius:12px;padding:7px;
    box-shadow:0 4px 10px rgba(0,0,0,.18)}
  .route-map{width:100%;height:100%;border-radius:6px;
    background:linear-gradient(135deg,#eef0e6 0%,#e3e6d6 50%,#d9e4ef 100%)}
  .tour-photo{position:absolute;width:80px;height:80px;border-radius:50%;border:4px solid var(--white);
    box-shadow:0 3px 8px rgba(0,0,0,.25)}

  .tour{position:absolute}
  .tour-kicker{display:block;font-weight:300;font-size:20px;line-height:1;color:var(--brand-blue)}
  .tour-name{display:block;font-weight:900;font-size:21px;line-height:1.05;color:var(--brand-blue);letter-spacing:.5px}
  .tour-copy{margin-top:6px;font-weight:600;font-size:9.5px;line-height:1.38;color:var(--ink);text-align:justify}
  .price{display:inline-block;margin-top:10px;padding:4px 14px;background:var(--brand-blue);
    color:var(--white);font-weight:800;font-size:14px;line-height:1.3;border-radius:3px}
</style>
</head>
<body>
<main class="spread">
  <div class="backdrop-photo" role="img" aria-label="Faint helicopter cockpit interior behind the tour listings"></div>
  <div class="fold"></div>

  <div class="photo photo-crew" role="img" aria-label="Pilot and crew beside a helicopter on a grass airfield"></div>
  <svg class="wave wave-top-left" viewBox="0 0 550 60" preserveAspectRatio="none" aria-hidden="true">
    <path d="M0 40 Q280 10 550 0 L550 60 L0 60Z" fill="var(--page-light)"/>
    <path d="M0 34 Q280 4 550 -6 L550 4 Q280 16 0 46Z" fill="var(--mid-blue)"/>
  </svg>
  <div class="photo photo-skyline" role="img" aria-label="Helicopter flying over a coastal city and bay"></div>
  <svg class="wave wave-top-right" viewBox="0 0 550 50" preserveAspectRatio="none" aria-hidden="true">
    <path d="M0 36 Q280 26 550 0 L550 50 L0 50Z" fill="var(--page-light)"/>
    <path d="M0 28 Q280 18 550 -8 L550 4 Q280 32 0 40Z" fill="var(--mid-blue)"/>
  </svg>

  <h1 class="section-title">SIGHTSEEING TOURS</h1>

  <!-- Quickie -->
  <section class="tour" style="left:40px;top:200px;width:240px">
    <h2><span class="tour-kicker">THE</span><span class="tour-name">QUICKIE</span></h2>
    <p class="tour-copy">Ready for a quick thrill? This is your chance! Take a ride to Downtown over Pellmont Bay, Heron Key and back! Experience Florida and Pellmont’s Skyline from your own magic carpet. This is a quick, affordable and adventure packed sightseeing tour for everyone’s budget. Available the 1st Saturday every month from 10am-3pm. Walk-in’s are encouraged, advanced reservations receive 10% OFF, prices are per person.</p>
    <span class="price">Price: $40.00</span>
  </section>
  <div class="map-card" style="left:300px;top:195px;width:220px;height:140px"><div class="route-map" role="img" aria-label="Route map of the Quickie tour"></div></div>
  <div class="tour-photo" style="left:330px;top:300px;background:linear-gradient(180deg,#6fb2e6,#3a7c9c 60%,#b89a70)" role="img" aria-label="Waterfront resort building"></div>

  <!-- Downtown & Romantic -->
  <div class="map-card" style="left:40px;top:440px;width:200px;height:145px"><div class="route-map" role="img" aria-label="Route map of the Downtown and Romantic tour"></div></div>
  <div class="tour-photo" style="left:70px;top:550px;background:linear-gradient(180deg,#c9b48a,#f1e4c2 50%,#8c7250)" role="img" aria-label="Glasses of champagne"></div>
  <section class="tour" style="left:265px;top:428px;width:260px">
    <h2><span class="tour-kicker">THE</span><span class="tour-name">DOWNTOWRN &amp;<br>ROMANTIC TOUR</span></h2>
    <p class="tour-copy">Our NEWEST helicopter tour includes romantic music and complimentary Champagne during your flight. Each tour is guaranteed to be private for a party of two (or up to 3 if requested) while experiencing the beauty of Downtown Pellmont and the surrounding islands. This Tour includes the sights of our DOWNTOWN Tour and is ideal for Anniversaries, Marriage proposals, etc</p>
    <span class="price">Price: $189.00</span>
  </section>

  <!-- Deluxe -->
  <div class="map-card" style="left:580px;top:215px;width:210px;height:135px"><div class="route-map" role="img" aria-label="Route map of the Deluxe tour"></div></div>
  <div class="tour-photo" style="left:610px;top:315px;background:linear-gradient(180deg,#4a86b8,#1e4f74 60%,#d5dde3)" role="img" aria-label="Cable-stayed bridge across the bay"></div>
  <section class="tour" style="left:815px;top:205px;width:250px">
    <h2><span class="tour-kicker">THE</span><span class="tour-name">DELUXE TOUR</span></h2>
    <p class="tour-copy">The special VIP Tour combines all the sights of our DOWNTOWN and ULTIMATE BEACH Tours and is our most exciting and exhilarating sightseeing option with many great locations and landmarks. This flight provides the opportunity to see virtually the entire Pellmont coastline with a trip across Marlin Bay along Seabright Causeway Bridge and Port Ardell Downtown.</p>
    <span class="price">Price: $295.00</span>
  </section>

  <!-- Ultimate Beach -->
  <section class="tour" style="left:590px;top:425px;width:250px">
    <h2><span class="tour-kicker">THE</span><span class="tour-name">ULTIMATE BEACH<br>TOUR</span></h2>
    <p class="tour-copy">Our NEWEST helicopter tour includes romantic music and complimentary Champagne during your flight. Each tour is guaranteed to be private for a party of two (or up to 3 if requested) while experiencing the beauty of Downtown Pellmont and the surrounding islands. This Tour includes the sights of our DOWNTOWN Tour and is ideal for Anniversaries, Marriage proposals, etc</p>
    <span class="price">Price: $159.00</span>
  </section>
  <div class="map-card" style="left:860px;top:440px;width:210px;height:135px"><div class="route-map" role="img" aria-label="Route map of the Ultimate Beach tour"></div></div>
  <div class="tour-photo" style="left:890px;top:540px;background:linear-gradient(160deg,#9fe0ea,#3fb3c9 50%,#e9e2cf)" role="img" aria-label="Turquoise beach shoreline from above"></div>

  <svg class="wave wave-bottom" viewBox="0 0 1100 40" preserveAspectRatio="none" aria-hidden="true">
    <path d="M0 24 Q550 8 1100 18 L1100 40 L0 40Z" fill="var(--mid-blue)"/>
    <path d="M0 32 Q550 16 1100 26 L1100 40 L0 40Z" fill="var(--brand-blue)"/>
  </svg>
</main>
</body>
</html>
```